Visitenkarten für Familienunternehmen in den Bereichen Fliesen, Natursteine, Kaminöfen, Schwimmbäder und Whirlpools
Zielgruppe
Wir sind ein Familienunternehmen in dritter Generation und Spezialist für Fliesen, Natursteine, Kaminöfen, Schwimmbäder und Whirlpools. Professionell, kreativ und voller Leidenschaft begleiten wir unsere Kunden bei der Umsetzung ihrer Vorhaben. Von der persönlichen Beratung bis hin zur Ausführung profitieren unsere Kunden von qualifiziertem Fachpersonal und 60 Jahren Erfahrung. Unsere Zielgruppe sind Familien/Paare ab 35 Jahren, die Produkte höchster Qualität für Ihr Zuhause suchen.
Aufgabenstellung
Wir benötigen neue Visitenkarten, da wir ein neues Logo haben. Wir haben folgende Vorstellung:
Rückseite: Komplett schwarz bzw. dunkel (Farbton ähnlich DB703), mittig unser neues Logo in weiß.
Vorderseite: Auch hier Hintergrund schwarz, Logo in weiß, Name des Ansprechpartners samt Titel/Position, Firmenname, Adresse, Telefonnummer, eMail-Adresse und Social Media-Adresse. Des Weiteren sollte unser Portfolio aufgelistet sein (Fliesen, Natursteine, Kaminöfen, Schwimmbäder und Whirlpools). Alternativ können wir uns die Auflistung des Portfolios auch auf der Rückseite vorstellen. Alternativ können wir uns die Vorderseite auch in weiß mit schwarzer Schrift vorstellen.
Der Inhalt der Datei, welche am Ende erstellt wird, muss für unsere Druckerei editierbar sein (Schrift als Text, nicht als Pfad).
Ergänzung 25.03.2023:
Nachdem die ersten Design-Vorschläge eingetroffen sind, haben wir uns dazu entschieden, dass es eine Visitenkarte im Querformat sein soll. Vorder- und Rückseite vollen schwarz/dunkel sein.

```html
<!DOCTYPE html>
<html lang="de">
<head>
<meta charset="utf-8">
<title>Visitenkarten Marmor Helm</title>
<link rel="stylesheet" href="https://fonts.googleapis.com/css2?family=Figtree:wght@400;700&family=Montserrat:wght@300&display=swap">
<style>
  :root {
    --stage: #ad8f68;
    --card-dark: #3b3736;
    --ink-on-dark: #ffffff;
    --rule-on-dark: #d9d4d0;
  }
  * { margin: 0; padding: 0; box-sizing: border-box; }
  html, body { width: 1200px; height: 846px; overflow: hidden; }
  body {
    position: relative;
    background: var(--stage);
    font-family: "Figtree", Arial, sans-serif;
    color: var(--ink-on-dark);
  }
  .card {
    position: absolute;
    width: 486px;
    height: 315px;
    background: var(--card-dark);
  }
  .card--back { left: 246px; top: 82px; }
  .card--front { left: 492px; top: 435px; }

  .wordmark {
    position: absolute;
    left: 0; right: 0;
    text-align: center;
    font-family: "Montserrat", Arial, sans-serif;
    font-weight: 300;
    line-height: 1;
    color: var(--ink-on-dark);
  }
  .card--back .wordmark {
    top: 119px;
    font-size: 54px;
    letter-spacing: 0.3em;
    padding-left: 0.3em;
  }
  .card--front .wordmark {
    top: 70px;
    font-size: 38px;
    letter-spacing: 0.3em;
    padding-left: 0.3em;
  }

  .contact {
    position: absolute;
    top: 156px;
    font-size: 15px;
    line-height: 21px;
    white-space: nowrap;
  }
  .contact--person { left: 34px; }
  .contact--person .contact__name,
  .contact--person .contact__company { font-weight: 700; line-height: 19px; }
  .contact--online { left: 294px; top: 175px; }
  .social { display: flex; align-items: center; gap: 8px; }
  .social__dot { width: 10px; height: 10px; border-radius: 50%; background: var(--ink-on-dark); }

  .divider {
    position: absolute;
    left: 31px; top: 265px;
    width: 423px; height: 1px;
    background: var(--rule-on-dark);
  }
  .portfolio {
    position: absolute;
    left: 34px; top: 279px;
    font-size: 15px;
    line-height: 18px;
    white-space: nowrap;
  }
</style>
</head>
<body>
  <section class="card card--back" aria-label="Rückseite">
    <div class="wordmark">HELM</div>
  </section>

  <section class="card card--front" aria-label="Vorderseite">
    <div class="wordmark">HELM</div>

    <div class="contact contact--person">
      <p class="contact__name">Timo Helm | Geschäftsführer</p>
      <p class="contact__company">Marmor Helm GmbH</p>
      <p>Lindenstr. 7 | 76829 Talheim</p>
      <p>Tel.: +49 (0)06 12 3 - 45 67 00</p>
    </div>

    <div class="contact contact--online">
      <p>info@marmor-helm.de</p>
      <p>www.marmor-helm.de</p>
      <p class="social"><span class="social__dot" aria-hidden="true"></span>@marmorhelm</p>
    </div>

    <div class="divider"></div>
    <p class="portfolio">Fliesen | Natursteine | Kaminöfen | Schwimmbäder | Whirlpools</p>
  </section>
</body>
</html>
```